2018 Brontor 3400 Velto construction

Eye catching and progressional design needed, not too busy, must integrate website, phone and our logo. We would like a complete wrap design covering the entire truck. I have a 2018 brontor 3400 crew cab. I am open to designs. Really want people to notice the company vehicle and remember the name and logo.

Target Market(s)

Middle class-to- high end clients

Industry/Entity Type

Construction

Font styles to use
Other font styles liked:
• Montserrat

Colors

Designer to choose colors to be used in the design.

Requirements
Must have
• Phone number: 555-417-2868 Website: Veltoconstruction.example Licensed and insured
Nice to have
• Bathrooms, kitchens, additions, new construction, remodeling

```html
<!DOCTYPE html>
<html lang="en">
<head>
<meta charset="utf-8">
<title>Velto Construction – Truck Wrap Concepts</title>
<link rel="stylesheet" href="https://fonts.googleapis.com/css2?family=Montserrat:wght@400&family=Poppins:wght@500;600&family=Oswald:wght@500&display=swap">
<style>
  :root {
    --tan: #e0a97c;
    --black: #0b0b0b;
    --white: #ffffff;
    --silver: #d9d9d9;
    --page: #ffffff;
  }
  html, body {
    margin: 0;
    padding: 0;
    overflow: hidden;
    background: var(--page);
  }
  .canvas {
    position: relative;
    width: 1200px;
    height: 1200px;
    overflow: hidden;
    background: var(--page);
  }
  .wrap-panel {
    position: absolute;
    left: 100px;
    width: 1000px;
    height: 330px;
  }
  .wrap-panel--gold-cab { top: 150px; }
  .wrap-panel--black-cab { top: 650px; }
  .wrap-panel__art {
    position: absolute;
    inset: 0;
    width: 100%;
    height: 100%;
  }
  .website {
    position: absolute;
    font-family: "Poppins", sans-serif;
    font-weight: 500;
    font-size: 15px;
    line-height: 1.2;
    margin: 0;
    white-space: nowrap;
  }
  .phone {
    position: absolute;
    font-family: "Poppins", sans-serif;
    font-weight: 600;
    font-size: 31px;
    letter-spacing: 1.5px;
    line-height: 1.2;
    margin: 0;
    white-space: nowrap;
  }
  .brand {
    position: absolute;
    display: flex;
    align-items: center;
    gap: 20px;
  }
  .brand__mark {
    width: 66px;
    height: 66px;
    border: 2px solid var(--tan);
    box-sizing: border-box;
    flex: none;
  }
  .brand__name {
    font-family: "Montserrat", sans-serif;
    font-weight: 400;
    font-size: 25px;
    letter-spacing: 4px;
    line-height: 1.3;
    color: var(--white);
    text-transform: uppercase;
    margin: 0;
    white-space: nowrap;
  }
  .licensed {
    position: absolute;
    font-family: "Oswald", sans-serif;
    font-weight: 500;
    font-size: 15px;
    color: var(--tan);
    text-transform: uppercase;
    margin: 0;
    white-space: nowrap;
  }
  .services {
    position: absolute;
    font-family: "Oswald", sans-serif;
    font-weight: 500;
    font-size: 13px;
    letter-spacing: 0.5px;
    text-transform: uppercase;
    margin: 0;
    white-space: nowrap;
  }
  /* concept one: tan cab, black belt */
  .wrap-panel--gold-cab .website { left: 62px; top: 72px; color: var(--tan); }
  .wrap-panel--gold-cab .phone { left: 58px; top: 92px; color: var(--white); }
  .wrap-panel--gold-cab .brand { left: 380px; top: 78px; }
  .wrap-panel--gold-cab .licensed { right: 50px; top: 106px; }
  .wrap-panel--gold-cab .services { left: 392px; top: 200px; color: var(--white); transform: rotate(1.6deg); transform-origin: left; }
  /* concept two: tan bed, black cab */
  .wrap-panel--black-cab .website { left: 62px; top: 66px; color: var(--black); }
  .wrap-panel--black-cab .phone { left: 26px; top: 86px; color: var(--black); }
  .wrap-panel--black-cab .brand { left: 400px; top: 78px; }
  .wrap-panel--black-cab .licensed { right: 50px; top: 96px; }
  .wrap-panel--black-cab .services { left: 400px; top: 261px; color: var(--black); }
</style>
</head>
<body>
<main class="canvas">

  <section class="wrap-panel wrap-panel--gold-cab" aria-label="Wrap concept with tan cab and black belt">
    <svg class="wrap-panel__art" viewBox="0 0 1000 330" preserveAspectRatio="none" aria-hidden="true">
      <rect class="panel-base" x="0" y="0" width="1000" height="330" fill="var(--tan)"/>
      <polygon class="belt" points="0,50 1000,80 1000,260 0,228" fill="var(--black)"/>
      <polyline class="pinstripe" points="0,168 370,178" fill="none" stroke="var(--tan)" stroke-width="5"/>
      <polyline class="pinstripe" points="370,236 1000,252" fill="none" stroke="var(--tan)" stroke-width="4"/>
    </svg>
    <p class="website">Veltoconstruction.example</p>
    <p class="phone">555-417-2868</p>
    <div class="brand">
      <div class="brand__mark"></div>
      <p class="brand__name">Velto<br>Construction</p>
    </div>
    <p class="licensed">Licensed and Insured</p>
    <p class="services">Bathrooms | Kitchens | Additions | New Construction | Remodeling</p>
  </section>

  <section class="wrap-panel wrap-panel--black-cab" aria-label="Wrap concept with tan bed and black cab">
    <svg class="wrap-panel__art" viewBox="0 0 1000 330" preserveAspectRatio="none" aria-hidden="true">
      <rect class="panel-base" x="0" y="0" width="1000" height="330" fill="var(--black)"/>
      <polygon class="bed-block" points="0,40 300,40 355,330 0,330" fill="var(--tan)"/>
      <polygon class="slash" points="312,40 330,40 384,300 366,300" fill="var(--silver)"/>
      <polygon class="service-strip" points="390,255 1000,255 1000,285 396,285" fill="var(--tan)"/>
    </svg>
    <p class="website">Veltoconstruction.example</p>
    <p class="phone">555-417-2868</p>
    <div class="brand">
      <div class="brand__mark"></div>
      <p class="brand__name">Velto<br>Construction</p>
    </div>
    <p class="licensed">Licensed and Insured</p>
    <p class="services">Bathrooms | Kitchens | Additions | New Construction | Remodeling</p>
  </section>

</main>
</body>
</html>
```